Flyer Template

I need a flyer template for door knocking on properties. Text Boxes need to be editable, with a header and text body. Footer to be my info. Project to be stylized to match my real estate signs and logo art from past projects

```html
<!DOCTYPE html>
<html lang="en">
<head>
<meta charset="utf-8">
<title>Brennan Realty – Door Knocking Flyer</title>
<link rel="stylesheet" href="https://fonts.googleapis.com/css2?family=Open+Sans:wght@400;600;700;800&family=Cinzel:wght@500;700&display=swap">
<style>
  :root {
    --brand-red: #ec2a33;
    --ink: #111111;
    --grey: #555555;
    --white: #ffffff;
    --page: #ffffff;
    --edge: #1a1a1a;
  }
  html, body {
    margin: 0;
    padding: 0;
    width: 1200px;
    height: 1200px;
    overflow: hidden;
    background: var(--page);
  }
  .flyer {
    position: absolute;
    left: 188px;
    top: 267px;
    width: 847px;
    height: 599px;
    background: var(--white);
    box-shadow: 0 0 4px rgba(0,0,0,0.25);
    overflow: hidden;
    font-family: "Open Sans", Arial, sans-serif;
  }
  .flyer-art {
    position: absolute;
    inset: 0;
    width: 847px;
    height: 599px;
  }
  .brand-name {
    position: absolute;
    left: 55px;
    top: 124px;
    width: 150px;
    margin: 0;
    text-align: center;
    font-weight: 800;
    font-size: 29px;
    line-height: 37px;
    color: var(--ink);
    letter-spacing: 0.5px;
  }
  .headline {
    position: absolute;
    left: 42px;
    top: 236px;
    margin: 0;
    font-size: 23px;
    line-height: 29px;
    font-weight: 400;
    color: var(--ink);
  }
  .headline .accent {
    display: block;
    font-weight: 700;
    color: var(--brand-red);
  }
  .body-copy {
    position: absolute;
    left: 41px;
    top: 334px;
    width: 500px;
    margin: 0;
    font-size: 13.4px;
    line-height: 17px;
    font-weight: 600;
    color: #1c1c1c;
  }
  .office-name {
    position: absolute;
    left: 41px;
    top: 488px;
    margin: 0;
    font-size: 20px;
    font-weight: 700;
    color: var(--grey);
    letter-spacing: -0.3px;
  }
  .disclaimer {
    position: absolute;
    left: 309px;
    top: 508px;
    margin: 0;
    font-family: "Cinzel", Georgia, serif;
    font-size: 12.5px;
    line-height: 17px;
    font-weight: 500;
    color: var(--white);
    letter-spacing: 0.4px;
  }
  .divider {
    position: absolute;
    left: 543px;
    top: 510px;
    width: 1.5px;
    height: 26px;
    background: var(--white);
  }
  .agent-name {
    position: absolute;
    left: 560px;
    top: 509px;
    margin: 0;
    font-family: "Cinzel", Georgia, serif;
    font-size: 19px;
    font-weight: 700;
    color: var(--white);
    letter-spacing: 0.6px;
  }
  .contact-row {
    position: absolute;
    left: 255px;
    top: 549px;
    display: flex;
    align-items: center;
    font-family: "Cinzel", Georgia, serif;
    font-weight: 700;
    font-size: 23px;
    color: var(--white);
  }
  .contact-row .icon { width: 26px; height: 26px; margin-right: 12px; }
  .contact-row .phone { margin-right: 18px; }
  .contact-row .email { font-size: 21px; letter-spacing: 0.3px; }
</style>
</head>
<body>
  <main class="flyer">
    <svg class="flyer-art" viewBox="0 0 847 599" xmlns="http://www.w3.org/2000/svg">
      <defs>
        <linearGradient id="hero-tones" x1="0" y1="0" x2="1" y2="0.4">
          <stop offset="0" stop-color="#e9e4df"/>
          <stop offset="0.3" stop-color="#7d93c4"/>
          <stop offset="0.6" stop-color="#8b3b52"/>
          <stop offset="0.85" stop-color="#b04a5d"/>
          <stop offset="1" stop-color="#f1f1f1"/>
        </linearGradient>
        <radialGradient id="portrait-tones" cx="0.5" cy="0.45" r="0.6">
          <stop offset="0" stop-color="#c7442e"/>
          <stop offset="0.7" stop-color="#9a2a22"/>
          <stop offset="1" stop-color="#3a3f4d"/>
        </radialGradient>
      </defs>

      <path class="hero-photo" role="img" aria-label="Couple holding a paper house cut-out"
            d="M178,0 C240,150 390,290 620,318 L847,288 L847,0 Z" fill="url(#hero-tones)"/>

      <path class="hero-swoosh" d="M159,0 L183,0 C230,130 310,215 370,235 C290,200 200,120 159,0 Z" fill="var(--brand-red)"/>
      <path class="hero-swoosh-right" d="M745,318 L847,292 L847,304 Z" fill="var(--brand-red)"/>

      <path class="footer-edge" d="M134,599 Q340,470 600,462 L760,470 Q820,490 847,545 L847,555 Q800,500 720,486 L600,472 Q360,480 150,599 Z" fill="var(--edge)"/>
      <path class="footer-band" d="M160,599 Q360,470 600,460 Q760,462 847,548 L847,599 Z" fill="var(--brand-red)"/>

      <circle cx="672" cy="389" r="107" fill="var(--white)"/>
      <circle class="agent-photo" role="img" aria-label="Portrait of the agent" cx="672" cy="389" r="99" fill="url(#portrait-tones)"/>
    </svg>

    <h1 class="brand-name">BRENNAN<br>REALTY</h1>

    <h2 class="headline">
      <span class="accent">WE BELIEVE CREATING</span>
      A BETTER WORLD STARTS WITH<br>HELPING OUR NEIGHBORS.
    </h2>

    <p class="body-copy">Lorem ipsum dolor sit amet, consectetur adipiscing elit, sed do eiusmod tempor incididunt ut labore et dolore magna aliqua. Quis ipsum sus-pendisse ultrices gravida. Risus commodo viverra maecenas accumsan lacus vel facilisis.</p>

    <p class="office-name">NORTHPOINT GROUP</p>

    <p class="disclaimer">EACH OFFICE INDEPENDENTLY<br>OWNER AND OPERATED</p>
    <span class="divider"></span>
    <p class="agent-name">JORDAN BRENNAN</p>

    <div class="contact-row">
      <svg class="icon" viewBox="0 0 24 24" aria-hidden="true">
        <path d="M6.6 10.8c1.4 2.8 3.8 5.1 6.6 6.6l2.2-2.2c.3-.3.7-.4 1-.2 1.1.4 2.3.6 3.6.6.6 0 1 .4 1 1V20c0 .6-.4 1-1 1C10.6 21 3 13.4 3 4c0-.6.4-1 1-1h3.5c.6 0 1 .4 1 1 0 1.3.2 2.5.6 3.6.1.3 0 .7-.2 1z" fill="var(--white)"/>
        <path d="M14 3.5a7 7 0 0 1 6.5 6.5M14 6.5a4 4 0 0 1 3.5 3.5" stroke="var(--white)" stroke-width="1.6" fill="none"/>
      </svg>
      <span class="phone">555-014-2287</span>
      <svg class="icon" viewBox="0 0 24 24" aria-hidden="true">
        <rect x="2" y="5" width="20" height="14" fill="none" stroke="var(--white)" stroke-width="1.8"/>
        <path d="M2 5l10 8 10-8M2 19l7.5-7M22 19l-7.5-7" fill="none" stroke="var(--white)" stroke-width="1.8"/>
      </svg>
      <span class="email">JBRENNAN@EXAMPLE.COM</span>
    </div>
  </main>
</body>
</html>
```